Business Card Design

We have recently seen two business cards that caught our attention and think the designs would work for us. We are an accounting firm that serves small businesses in a variety of industries. Attached are the two business card that inspired us along with very rough layouts. We would like to see a professional layout using our company information.

Industry/Entity Type

Accounting

Contact Information for Business Card

Company Name - Dalworth Pryce
Address - 4180 Brambleton Lane, Suite 310, Houston, TX 77051
713-508-9627 - Main
281-369-0714 - Fax

Team Member Names, emails and phone numbers (see attachment)

```html
<!DOCTYPE html>
<html lang="en">
<head>
<meta charset="utf-8">
<title>Dalworth Pryce – Business Card</title>
<link rel="stylesheet" href="https://fonts.googleapis.com/css2?family=Crimson+Text:wght@400&display=swap">
<style>
  :root {
    --backdrop: #e7e5e1;
    --card: #ffffff;
    --band-light: #939396;
    --band-dark: #55555a;
    --ink: #1c1c1c;
    --label: #c9c9cc;
    --on-band: #ffffff;
  }
  * { margin: 0; padding: 0; box-sizing: border-box; }
  html, body {
    width: 1200px; height: 1000px; overflow: hidden;
    background: var(--backdrop);
  }
  .canvas { position: relative; width: 1200px; height: 1000px; }
  .card {
    position: absolute; left: 310px; top: 57px;
    width: 580px; height: 886px;
    background: var(--card);
    overflow: hidden;
    font-family: "Crimson Text", Georgia, serif;
    color: var(--ink);
    box-shadow: 0 6px 18px rgba(0,0,0,0.18);
  }
  .bands { position: absolute; inset: 0; width: 100%; height: 100%; }
  .company-name {
    position: absolute; left: 0; right: 0; top: 290px;
    text-align: center; font-size: 48px; letter-spacing: 0.5px;
  }
  .holder { position: absolute; left: 112px; top: 430px; }
  .holder-name { font-size: 54px; line-height: 1; }
  .holder-title {
    font-size: 23px; color: var(--on-band);
    margin-left: 112px; margin-top: 6px; letter-spacing: 0.4px;
  }
  .address {
    position: absolute; left: 132px; top: 598px;
    font-size: 23px; line-height: 31px;
  }
  .phones {
    position: absolute; left: 136px; top: 676px;
    list-style: none; font-size: 23px; line-height: 29px;
  }
  .phone-label { color: var(--label); }
</style>
</head>
<body>
<main class="canvas">
  <article class="card">
    <svg class="bands" viewBox="0 0 445 680" preserveAspectRatio="none" aria-hidden="true">
      <polygon fill="var(--band-light)" points="0,295 445,405 445,520 0,400"/>
      <polygon fill="var(--band-light)" points="0,585 330,680 0,680"/>
      <polygon fill="var(--band-dark)" points="0,585 445,505 445,560 150,640"/>
    </svg>

    <div class="company-name">Dalworth Pryce</div>

    <div class="holder">
      <div class="holder-name">Marisol Avery</div>
      <div class="holder-title">Account Manager</div>
    </div>

    <address class="address" style="font-style:normal">
      4180 Brambleton Lane, Suite 310<br>
      Houston, TX 77051
    </address>

    <ul class="phones">
      <li>713-508-9627 – <span class="phone-label">Main</span></li>
      <li>713-615-2048 – <span class="phone-label">Direct</span></li>
      <li>832-470-3195 - <span class="phone-label">Mobile</span></li>
    </ul>
  </article>
</main>
</body>
</html>
```